KVOR Membership Web Design Project

We need a website design for KVOR membership. We need something different from what we currently have. See what we currently have: http://www.travsel.example/mlm2/

Make provision for where members bushiness can be advertised.
Updates

We need a box for advertising members projects/business.

Make provision for where members bushiness / products can be advertised.

Target Market(s)

For members of KVOR and Intending members. Membership is for married men only.

Requirements
Must have
• Make provision for where members bushiness can be advertised.

You are to redesign: http://www.travsel.example/mlm2/

```html
<!DOCTYPE html>
<html lang="en">
<head>
<meta charset="utf-8">
<title>KVOR Fellowship</title>
<link href="https://fonts.googleapis.com/css2?family=Source+Sans+3:wght@400;600;700&family=Open+Sans:ital,wght@1,400&display=swap" rel="stylesheet">
<style>
:root{
  --sky:#f1f7fb;
  --navy:#0d4479;
  --navy-dark:#0b3a69;
  --green:#6a9a1c;
  --green-light:#93be34;
  --green-dark:#4f830f;
  --link:#1a5294;
  --text:#555;
  --rule:#9a9a9a;
  --side:#f1f3f3;
}
*{margin:0;padding:0;box-sizing:border-box}
html,body{width:1145px;height:1200px;overflow:hidden}
body{position:relative;background:var(--sky);font-family:"Source Sans 3",Arial,sans-serif;color:var(--text)}
.abs{position:absolute}
.band{left:0;top:178px;width:1145px;height:372px;background:var(--navy)}
.content-bg{left:0;top:550px;width:1145px;height:553px;background:#fff}
.footer{left:0;top:1103px;width:1145px;height:97px;background:var(--navy-dark);text-align:center;color:#fff;font-size:12.5px}
.footer nav{margin-top:30px}
.footer nav span{margin:0 7px;opacity:.9}
.footer p{margin-top:11px}

.brand{left:52px;top:30px;display:flex;align-items:center;gap:14px}
.brand-mark{width:98px;height:98px;border-radius:50%;background:var(--navy)}
.brand-name{font-size:34px;font-weight:600;color:var(--navy)}

.search{left:720px;top:0;width:376px;height:57px;background:#fff;border-radius:0 0 8px 8px;box-shadow:0 1px 4px rgba(0,0,0,.12)}
.search-input{left:18px;top:15px;width:260px;height:27px;border:1px solid #b9b9b9;border-radius:3px;background:#fff}
.search-btn{left:287px;top:15px;width:74px;height:27px;border-radius:3px;background:linear-gradient(#a8c86a,#7aa53a);color:#fff;font-size:12px;font-weight:700;text-align:center;line-height:27px;letter-spacing:.5px}
.connect{left:836px;top:85px;font-style:italic;font-size:13px;color:#777}
.social{top:76px;width:34px;height:34px;border-radius:50%;background:var(--navy)}

.nav{left:49px;top:154px;width:1046px;height:41px;border-radius:14px 14px 0 0;background:linear-gradient(var(--green-light),var(--green-dark));display:flex;color:#fff;font-size:14.5px}
.nav div{display:flex;align-items:center;justify-content:center;border-right:1px solid rgba(255,255,255,.25);gap:6px}
.nav .caret{width:0;height:0;border-left:4px solid transparent;border-right:4px solid transparent;border-top:4px solid #fff}
.nav .home{width:68px;background:rgba(0,0,0,.15);border-radius:14px 0 0 0}
.nav .login{flex:1;border-right:0;background:rgba(0,0,0,.12);border-radius:0 14px 0 0}

.hero{left:48px;top:195px;width:1046px;height:353px;background:linear-gradient(180deg,#3e6fa8 0%,#7ea3c9 40%,#d9a99a 68%,#d27b5c 85%,#2a1b1b 100%)}
.hero-title{left:780px;top:240px;font-family:"Open Sans",Arial,sans-serif;font-style:italic;font-size:36px;color:#fff;text-shadow:0 1px 3px rgba(0,0,0,.4)}
.dot{top:503px;width:16px;height:16px;border-radius:50%;border:3px solid var(--green)}
.dot.on{background:#0b2a10}

h2{color:var(--green);font-weight:600}
.welcome{left:50px;top:573px;font-size:25px}
.intro{left:50px;top:622px;width:715px;font-size:12.3px;line-height:21.8px;text-align:justify}
.dotted{border-top:1.5px dotted var(--rule)}

.icon{border-radius:8px}
.feat-title{font-size:17px}
.feat-links{font-size:15px;color:var(--link);font-weight:600}
.feat-links i{font-style:normal;color:var(--navy);margin:0 8px}
.feat-text{width:255px;font-size:12.5px;line-height:19.5px;text-align:justify}
.vline{width:1px;background:#ccc}
.hline{height:1px;background:#bbb}

.saving{left:426px;top:958px;width:334px;height:125px;border-radius:10px;border:3px solid #e2ebcf;background:linear-gradient(180deg,#3f7ec4,#a9cbe6 70%,#6d8a3a);overflow:hidden}
.saving p{position:absolute;left:22px;top:28px;color:#fff;font-size:17px;line-height:1.25}
.saving b{display:block;font-size:24px;color:#b8e06a;font-weight:700}

.side{left:786px;top:552px;width:309px;height:531px;background:var(--side)}
.side-title{font-size:17px}
.proj-name{font-size:17px;color:var(--link);font-weight:600}
.proj-sub{font-size:12px;margin-top:3px}
.side-links a{position:absolute;font-size:15px;color:var(--link);font-weight:600;text-decoration:none}
</style>
</head>
<body>
<div class="abs band"></div>
<div class="abs content-bg"></div>

<header>
  <div class="abs brand"><span class="brand-mark"></span><span class="brand-name">KVOR</span></div>
  <div class="abs search">
    <div class="abs search-input"></div>
    <div class="abs search-btn">SEARCH</div>
  </div>
  <div class="abs connect">Connect with us :</div>
  <span class="abs social" style="left:948px" role="img" aria-label="Social network link"></span>
  <span class="abs social" style="left:995px" role="img" aria-label="Social network link"></span>
  <span class="abs social" style="left:1043px" role="img" aria-label="Social network link"></span>
</header>

<nav class="abs nav">
  <div class="home"><svg width="17" height="15" viewBox="0 0 17 15"><path d="M8.5 0 0 7.5h2.5V15h4.5v-5h3v5h4.5V7.5H17z" fill="#fff"/></svg></div>
  <div style="width:113px">About us <span class="caret"></span></div>
  <div style="width:141px">Membership <span class="caret"></span></div>
  <div style="width:172px">Member Projects <span class="caret"></span></div>
  <div style="width:180px">Membership Levels <span class="caret"></span></div>
  <div style="width:99px">Links <span class="caret"></span></div>
  <div style="width:124px">Contact us <span class="caret"></span></div>
  <div class="login"><svg width="15" height="14" viewBox="0 0 15 14"><circle cx="7.5" cy="4" r="3.6" fill="#fff"/><path d="M0 14c0-4 3.4-6 7.5-6S15 10 15 14z" fill="#fff"/></svg> Login</div>
</nav>

<div class="abs hero" role="img" aria-label="Silhouette of a praying man before a cross against a cloudy sunset sky"></div>
<div class="abs hero-title">Hope Circle</div>
<span class="abs dot on" style="left:897px"></span>
<span class="abs dot" style="left:930px"></span>
<span class="abs dot" style="left:962px"></span>
<span class="abs dot" style="left:995px"></span>
<span class="abs dot" style="left:1027px"></span>

<main>
  <h2 class="abs welcome">Welcome to our site</h2>
  <p class="abs intro">Sed ut perspiciatis unde omnis iste natus error sit voluptatem accusantium doloremque laudantium, totam rem aperiam, eaque ipsa quae ab illo inventore veritatis et quasi architecto beatae vitae dicta sunt explicabo. Nemo enim ipsam voluptatem quia voluptas sit aspernatur aut odit aut fugit, sed quia consequuntur magni dolores eos qui ratione voluptatem sequi nesciunt. Neque porro quisquam est, qui dolorem ipsum quia dolor sit amet, consectetur, adipisci velit, sed quia non numquam eius modi tempora incidunt ut labore et dolore magnam aliquam quaerat voluptatem. Ut enim ad minima veniam, quis nostrum exercitationem ullam corporis suscipit laboriosam, nisi ut aliquid ex ea commodi consequatur</p>
  <div class="abs dotted" style="left:50px;top:777px;width:712px"></div>

  <span class="abs icon" style="left:52px;top:808px;width:52px;height:72px;background:#f4c81c" role="img" aria-label="Glowing light bulb"></span>
  <h2 class="abs feat-title" style="left:117px;top:801px">Our Objectives</h2>
  <div class="abs feat-links" style="left:119px;top:836px">Who we are<i>|</i>What we do</div>
  <p class="abs feat-text" style="left:119px;top:866px">Nemo enim ipsam voluptatem quia voluptas sit aspernatur aut odit aut fugit, sed quia consequuntur magni dolores.</p>

  <div class="abs vline" style="left:402px;top:800px;height:135px"></div>

  <span class="abs icon" style="left:424px;top:808px;width:50px;height:72px;background:#6b7a86" role="img" aria-label="Businessman illustration"></span>
  <h2 class="abs feat-title" style="left:489px;top:801px">Membership Levels / Benefits</h2>
  <div class="abs feat-links" style="left:491px;top:836px">Gold<i>|</i>Silver<i>|</i>Premium</div>
  <p class="abs feat-text" style="left:491px;top:866px">Nemo enim ipsam voluptatem quia voluptas sit aspernatur aut odit aut fugit, sed quia consequuntur magni dolores.</p>

  <div class="abs hline" style="left:49px;top:939px;width:329px"></div>
  <div class="abs hline" style="left:422px;top:939px;width:338px"></div>

  <span class="abs icon" style="left:52px;top:962px;width:52px;height:72px;background:#f4c81c" role="img" aria-label="Glowing light bulb"></span>
  <h2 class="abs feat-title" style="left:117px;top:955px">Registration</h2>
  <div class="abs feat-links" style="left:119px;top:990px">Join the KVOR</div>
  <p class="abs feat-text" style="left:119px;top:1020px">Nemo enim ipsam voluptatem quia voluptas sit aspernatur aut odit aut fugit, sed quia consequuntur magni dolores.</p>

  <div class="abs vline" style="left:402px;top:960px;height:124px"></div>

  <div class="abs saving" role="img" aria-label="Hand dropping a coin into a piggy bank under a blue sky">
    <p>Learn the<b>Saving Culture</b></p>
  </div>
</main>

<aside class="abs side">
  <h2 class="abs side-title" style="left:16px;top:27px">Members Projects</h2>
  <div class="abs dotted" style="left:16px;top:68px;width:278px"></div>

  <span class="abs icon" style="left:17px;top:88px;width:48px;height:48px;background:#4d8fd0" role="img" aria-label="Printer icon"></span>
  <div class="abs" style="left:90px;top:90px"><div class="proj-name">Harvest Project</div><div class="proj-sub">Savings / Co-operative society culture</div></div>

  <span class="abs icon" style="left:17px;top:160px;width:48px;height:44px;background:#e9c55a" role="img" aria-label="Envelope icon"></span>
  <div class="abs" style="left:90px;top:162px"><div class="proj-name">Bulk SMS</div><div class="proj-sub">Bulk SMS Service for members</div></div>

  <span class="abs icon" style="left:22px;top:226px;width:40px;height:50px;background:#8a8d90" role="img" aria-label="Padlock icon"></span>
  <div class="abs" style="left:90px;top:231px"><div class="proj-name">Builders Guild</div><div class="proj-sub">KVOR Construction Outfit</div></div>

  <span class="abs icon" style="left:26px;top:296px;width:32px;height:46px;background:#2a9bc8" role="img" aria-label="Dollar sign icon"></span>
  <div class="abs" style="left:90px;top:301px"><div class="proj-name">Hope Circle</div><div class="proj-sub">The Ultimate savings scheme</div></div>

  <h2 class="abs side-title" style="left:16px;top:376px">Links</h2>
  <div class="abs dotted" style="left:16px;top:416px;width:278px"></div>
  <div class="side-links">
    <a style="left:17px;top:438px">KVOR Website</a>
    <a style="left:149px;top:438px">Builders Guild</a>
    <a style="left:17px;top:469px">SMS Portal</a>
    <a style="left:149px;top:469px">Co-operative portal</a>
  </div>
</aside>

<footer class="abs footer">
  <nav>Home<span>|</span>About us<span>|</span>Membership<span>|</span>Member Projects<span>|</span>Membership Levels<span>|</span>Links<span>|</span>Contact us<span>|</span>Login</nav>
  <p>Copyright © 2012 www.kvor.example&nbsp; All rights reserved.</p>
</footer>
</body>
</html>
```